Auto glass company

BRIGHTWAY
Roving Auto Glass, LLC
555-604-1937

* Windshield Replacement
* Rock Chip Repair
Danny "K"
Brightwayrovingautoglass@example.com
* Fully Insured

This is what I would like on the card. The image is what I had before. Looking for a logo possible too, couldn’t find a place to add that on. It’s a auto glass company.

Target Market(s)

Auto glass

Industry/Entity Type

Auto glass

Contact Information for Business Card

Logo, business name, phone number, windshield replacement, rock chip repair, insured, owner name Danny K, email address brightwayrovingautoglass@example.com

Colors

Designer to choose colors to be used in the design.

Requirements
Must have
• Logo, business name, phone number, windshield replacement, rock chip repair, insured, owner name Danny K, email address brightwayrovingautoglass@example.com

```html
<!DOCTYPE html>
<html lang="en">
<head>
<meta charset="utf-8">
<title>Brightway Roving Auto Glass – Business Card</title>
<link href="https://fonts.googleapis.com/css2?family=Montserrat:wght@400;500;600;700;800&family=Abril+Fatface&family=Red+Hat+Display:wght@400;500&display=swap" rel="stylesheet">
<style>
  :root {
    --page-bg: #ececec;
    --card-black: #050505;
    --card-edge: #1e1e20;
    --brand-blue: #1a9be0;
    --brand-blue-deep: #2f7fd0;
    --text-white: #ffffff;
    --title-ink: #151515;
  }
  * { margin: 0; padding: 0; box-sizing: border-box; }
  html, body {
    width: 1200px; height: 971px; overflow: hidden;
    background: var(--page-bg);
  }
  .sheet { position: relative; width: 1200px; height: 971px; }

  .sheet-label {
    position: absolute; left: 750px; top: 44px;
    font-family: "Red Hat Display", sans-serif; color: var(--title-ink);
  }
  .sheet-label__title { font-size: 36px; font-weight: 500; letter-spacing: -0.5px; }
  .sheet-label__size { font-size: 25px; font-weight: 400; margin-top: 8px; }

  .card {
    position: absolute; width: 560px; height: 320px;
    background: linear-gradient(160deg, var(--card-edge) 0%, var(--card-black) 45%);
    box-shadow: 0 10px 24px rgba(0,0,0,0.35);
    font-family: "Montserrat", sans-serif; color: var(--text-white);
    overflow: hidden;
  }
  .card--contact { left: 90px; top: 170px; }
  .card--brand { left: 560px; top: 570px; }

  /* brand lockup */
  .brand { display: flex; align-items: center; gap: 10px; }
  .brand__square { width: 16px; height: 16px; background: var(--brand-blue); flex: none; }
  .brand__name { font-weight: 800; color: var(--brand-blue); letter-spacing: 0.5px; line-height: 1; }
  .brand__tagline { font-weight: 600; text-transform: uppercase; letter-spacing: 0.6px; color: var(--text-white); }

  /* contact side */
  .card--contact .brand-block { position: absolute; right: 40px; top: 44px; text-align: right; }
  .card--contact .brand__name { font-size: 30px; }
  .card--contact .brand__tagline { font-size: 9px; margin-top: 5px; }

  .services { position: absolute; left: 40px; top: 48px; list-style: none; }
  .services li {
    display: flex; align-items: center; gap: 10px;
    font-size: 15px; font-weight: 500; line-height: 22px; color: var(--text-white);
  }
  .services li::before {
    content: ""; width: 9px; height: 9px; border-radius: 50%;
    border: 2.5px solid var(--brand-blue); flex: none;
  }

  .phone {
    position: absolute; right: 40px; top: 150px;
    font-size: 27px; font-weight: 700; letter-spacing: 0.5px;
  }

  .owner { position: absolute; left: 40px; top: 200px; }
  .owner__name { font-family: "Abril Fatface", serif; font-size: 38px; line-height: 1; }
  .owner__first { color: var(--brand-blue); }
  .owner__nick { color: var(--text-white); font-size: 30px; }
  .owner__role { font-size: 14px; font-weight: 600; margin-top: 2px; }

  .email {
    position: absolute; left: 40px; bottom: 26px;
    display: flex; align-items: center; gap: 12px;
    font-size: 14px; font-weight: 500; letter-spacing: 0.3px;
  }
  .email svg { width: 22px; height: 16px; flex: none; }

  /* brand side */
  .card--brand .brand-block {
    position: absolute; left: 0; right: 0; top: 88px;
    display: flex; flex-direction: column; align-items: center;
  }
  .card--brand .brand__square { width: 26px; height: 26px; }
  .card--brand .brand__name { font-size: 54px; }
  .card--brand .brand__tagline { font-size: 14px; margin-top: 8px; }
  .tagline-strip {
    position: absolute; left: 0; right: 0; bottom: 44px; text-align: center;
    font-size: 16px; font-weight: 500; letter-spacing: 0.5px;
  }
</style>
</head>
<body>
<main class="sheet">
  <header class="sheet-label">
    <div class="sheet-label__title">Business Card- Mockup 1</div>
    <div class="sheet-label__size">Size: 3.5in X 2.0 in</div>
  </header>

  <section class="card card--contact" aria-label="Business card, contact side">
    <ul class="services">
      <li>Windshield Replacement</li>
      <li>Rock Chip Repair</li>
      <li>Fully Insured</li>
    </ul>

    <div class="brand-block">
      <div class="brand" style="justify-content:flex-end">
        <span class="brand__square"></span>
        <span class="brand__name">BRIGHTWAY</span>
      </div>
      <div class="brand__tagline">Roving Auto Glass, LLC</div>
    </div>

    <div class="phone">555-604-1937</div>

    <div class="owner">
      <div class="owner__name"><span class="owner__first">Danny</span> <span class="owner__nick">"K"</span></div>
      <div class="owner__role">owner</div>
    </div>

    <div class="email">
      <svg viewBox="0 0 22 16" aria-hidden="true">
        <rect x="1" y="1" width="20" height="14" fill="none" stroke="var(--brand-blue)" stroke-width="2"/>
        <polyline points="1,1 11,9 21,1" fill="none" stroke="var(--brand-blue)" stroke-width="2"/>
      </svg>
      <span>brightwayrovingautoglass@example.com</span>
    </div>
  </section>

  <section class="card card--brand" aria-label="Business card, brand side">
    <div class="brand-block">
      <div class="brand">
        <span class="brand__square"></span>
        <span class="brand__name">BRIGHTWAY</span>
      </div>
      <div class="brand__tagline">Roving Auto Glass, LLC</div>
    </div>
    <div class="tagline-strip">Windshield Replacement / Rock Chip Repair / Fully Insured</div>
  </section>
</main>
</body>
</html>
```